Natural Health Supplement Company Needs a Product Label Designed

HARVEST ROOT LABS needs a PROBIOTICS product label designed.We are a natural health vitamin and dietary supplement company. Who ever wins will have the opportunity to design a lot more product labels for us.
Product name: PROBIOTICS
*Please use the attached logo and base the label text exactly off the Kelt Wellness label example.
Other product examples have been attached for inspiration.

Colors

Designer to choose colors to be used in the design.

Requirements
Must have
• Product name: PROBIOTICS
• *Please use the attached logo and base the label text exactly off the Kelt Wellness label example.
• Other product examples have been attached for inspiration.

```html
<!DOCTYPE html>
<html lang="en">
<head>
<meta charset="utf-8">
<title>Harvest Root Labs – Probiotics Label</title>
<link rel="stylesheet" href="https://fonts.googleapis.com/css2?family=Oswald:wght@700&family=Open+Sans:wght@600&family=Cinzel:wght@400;700&display=swap">
<style>
  :root {
    --green: #5fbf1f;
    --green-light: #7fd83a;
    --green-dark: #2f7a12;
    --title-top: #4ea21a;
    --title-bottom: #1f5a0c;
    --silver-1: #ffffff;
    --silver-2: #e6e8e8;
    --silver-3: #c9cccc;
    --bar-grey: #6b6d6e;
    --white: #ffffff;
  }
  html, body {
    margin: 0;
    padding: 0;
    overflow: hidden;
  }
  .label {
    position: relative;
    width: 1200px;
    height: 1103px;
    overflow: hidden;
    background: linear-gradient(90deg, var(--silver-3) 0%, var(--silver-1) 22%, var(--silver-2) 50%, var(--silver-1) 78%, var(--silver-3) 100%);
    font-family: "Open Sans", sans-serif;
  }
  .label__shapes {
    position: absolute;
    inset: 0;
  }
  .brand {
    position: absolute;
    top: 182px;
    left: 0;
    width: 1200px;
    text-align: center;
    font-family: "Cinzel", serif;
    font-weight: 700;
    font-size: 44px;
    line-height: 1;
    letter-spacing: 2px;
    color: var(--green);
    margin: 0;
  }
  .product-name {
    position: absolute;
    top: 300px;
    left: 0;
    width: 1200px;
    text-align: center;
    margin: 0;
    font-family: "Oswald", sans-serif;
    font-weight: 700;
    font-size: 168px;
    line-height: 1;
    letter-spacing: 2px;
    background: linear-gradient(180deg, var(--title-top), var(--title-bottom));
    -webkit-background-clip: text;
    background-clip: text;
    color: transparent;
  }
  .tech-bar {
    position: absolute;
    top: 512px;
    left: 0;
    width: 1200px;
    text-align: center;
    color: var(--white);
    font-size: 42px;
    line-height: 60px;
    margin: 0;
  }
  .badge-text {
    position: absolute;
    width: 200px;
    text-align: center;
    color: var(--white);
    font-family: "Cinzel", serif;
    line-height: 1;
  }
  .badge-text__big { display: block; font-size: 72px; }
  .badge-text__small { display: block; font-size: 26px; }
  .badge-text--acid .badge-text__small { font-size: 34px; line-height: 1.05; }
  .badge-text--acid .badge-text__tiny { display: block; font-size: 24px; }
  .benefit {
    position: absolute;
    top: 866px;
    left: 0;
    width: 1200px;
    text-align: center;
    color: var(--white);
    font-size: 40px;
    line-height: 1.3;
    margin: 0;
  }
  .footer-line {
    position: absolute;
    top: 1028px;
    left: 0;
    width: 1200px;
    text-align: center;
    color: var(--white);
    font-size: 36px;
    margin: 0;
    letter-spacing: 0.5px;
  }
  .footer-line__divider { margin: 0 24px; }
</style>
</head>
<body>
<main class="label">
  <svg class="label__shapes" width="1200" height="1103" viewBox="0 0 1200 1103" aria-hidden="true">
    <defs>
      <linearGradient id="badgeFill" x1="0" y1="0" x2="0" y2="1">
        <stop offset="0" stop-color="#7fd83a"/>
        <stop offset="1" stop-color="#3f9a14"/>
      </linearGradient>
      <linearGradient id="badgeDark" x1="0" y1="0" x2="0" y2="1">
        <stop offset="0" stop-color="#3e8a14"/>
        <stop offset="1" stop-color="#1f5a0c"/>
      </linearGradient>
      <linearGradient id="silverRim" x1="0" y1="0" x2="0" y2="1">
        <stop offset="0" stop-color="#ffffff"/>
        <stop offset="1" stop-color="#9fa3a3"/>
      </linearGradient>
    </defs>

    <!-- top frame line with brand cradle -->
    <path d="M0 92 H200 C260 92 250 300 340 300 H860 C950 300 940 92 1000 92 H1200"
          fill="none" stroke="#b9bcbc" stroke-width="14"/>
    <path d="M0 80 H200 C260 80 250 288 340 288 H860 C950 288 940 80 1000 80 H1200"
          fill="none" stroke="var(--green)" stroke-width="10"/>

    <!-- technology bar -->
    <path d="M210 512 H990 L960 572 H240 Z" fill="var(--bar-grey)"/>

    <!-- badges -->
    <g transform="translate(300 700)">
      <polygon points="0,-112 97,-56 97,56 0,112 -97,56 -97,-56" fill="url(#silverRim)"/>
      <polygon points="0,-100 87,-50 87,50 0,100 -87,50 -87,-50" fill="url(#badgeFill)"/>
    </g>
    <g transform="translate(600 700)">
      <polygon points="0,-112 97,-56 97,56 0,112 -97,56 -97,-56" fill="url(#silverRim)"/>
      <polygon points="0,-100 87,-50 87,50 0,100 -87,50 -87,-50" fill="url(#badgeDark)"/>
    </g>
    <g transform="translate(900 700)">
      <polygon points="0,-112 97,-56 97,56 0,112 -97,56 -97,-56" fill="url(#silverRim)"/>
      <polygon points="0,-100 87,-50 87,50 0,100 -87,50 -87,-50" fill="url(#badgeFill)"/>
    </g>

    <!-- lower green band with raised panel -->
    <path d="M0 1000 H250 C320 1000 300 830 380 830 H820 C900 830 880 1000 950 1000 H1200 V1103 H0 Z"
          fill="#b9bcbc"/>
    <path d="M0 1012 H255 C325 1012 305 842 385 842 H815 C895 842 875 1012 945 1012 H1200 V1103 H0 Z"
          fill="var(--green)"/>
  </svg>

  <p class="brand">HARVEST ROOT LABS</p>
  <h1 class="product-name">PROBIOTICS</h1>
  <p class="tech-bar">Bi-Pass Technology</p>

  <div class="badge-text" style="left:200px; top:632px;">
    <span class="badge-text__big">40</span>
    <span class="badge-text__small">BILLION<br>CFU</span>
  </div>
  <div class="badge-text" style="left:500px; top:640px;">
    <span class="badge-text__big">11</span>
    <span class="badge-text__small">STRAINS</span>
  </div>
  <div class="badge-text badge-text--acid" style="left:800px; top:650px;">
    <span class="badge-text__small">ACID<br>&amp; BILE</span>
    <span class="badge-text__tiny">RESISTANT</span>
  </div>

  <p class="benefit">For Optimal Digestive<br>and Immune Health</p>
  <p class="footer-line">DIETARY SUPPLEMENT<span class="footer-line__divider">|</span>30 CAPULES</p>
</main>
</body>
</html>
```